Startup High Tech Software Company Needs a Web Design (4 pages)

We need a web design for a startup high tech software company based in Brazil called Vexlo. We are known to build extremely fast softwares with high qualities for web and mobile (Robo OS and Orbit OS) applications.
We still don't have all the content to build the institutional web site, but we'd like to have the design already so we can change the content on demand later.
Basically we're requesting a home page and 3 templates of internal pages with spaces to videos and images.
Below are some examples of sites (please ignore the style, this is just to show the distribution of the main content):
Home: http://www.prondel.com.br/
Internal pages: http://www.qorvath.com/brightglobe/us/en/embedded_systems/industries/index.html
http://www-01.qorvath.com/software/lucent/solutions/automotive/
http://www.qorvath.com/brightglobe/us/en/embedded_systems/overview/index.html?lnk=ushpls1

The header and footer of Qorvath's web site's positions looks good for us (not the same style).

The first impression should be representing exactly what we are, fast and innovative company with high quality professionals.

Please consider the logos attached. We'd like to have a web site that combines with these logos. You can use either one (horizontal or vertical) depending on the place it is located.

Target Market(s)

CIO, IT managers of mid to big size companies

Industry/Entity Type

Automotive

Requirements
Must have
• HTML, CSS (responsive CSS is preferred) and images like buttons with no text inside, because the web site is going to have different languages so we can edit them easily.
Like Qorvath, some link or combobox to change the language.
Nice to have
• Timer to change the main content of the home page (not flash).
Should not have
• Flash

```html
<!DOCTYPE html>
<html lang="en">
<head>
<meta charset="utf-8">
<title>Vexlo – Home</title>
<link href="https://fonts.googleapis.com/css2?family=Open+Sans:wght@400;600&family=Arimo:wght@400;700&display=swap" rel="stylesheet">
<style>
  :root{
    --navy:#1f3b68;
    --navy-dark:#162d52;
    --brand:#2b4b7c;
    --header-bg:#e9eff4;
    --hero-bg:#f3f4f5;
    --text:#666;
    --title:#23407a;
    --btn-bg:#ececec;
    --footer-bg:#363636;
    --footer-bottom:#2b2b2b;
    --footer-head:#6cc4ee;
    --footer-link:#d8d8d8;
  }
  *{box-sizing:border-box;margin:0;padding:0}
  html,body{width:1015px;height:1200px;overflow:hidden}
  body{position:relative;background:#fff;font-family:"Arimo",Arial,sans-serif;color:var(--text)}
  .abs{position:absolute}

  .topbar{left:0;top:0;width:1015px;height:42px;background:linear-gradient(#294a7c,var(--navy-dark))}
  .account{left:602px;top:14px;color:#fff;font-size:11px;letter-spacing:.2px}
  .search{left:717px;top:8px;width:142px;height:25px;background:#fff;border:1px solid #c9d2dc;font-size:10px;padding:7px 10px;color:#333}
  .search svg{position:absolute;right:7px;top:5px}
  .lang{left:868px;top:8px;width:72px;height:25px;background:#fff;border:1px solid #c9d2dc;font-size:10px;color:#333;padding:6px 0 0 27px}
  .lang .flag{position:absolute;left:8px;top:8px;width:13px;height:9px;background:#2c4c8c}
  .lang svg{position:absolute;right:9px;top:10px}

  .masthead{left:0;top:42px;width:1015px;height:75px;background:var(--header-bg)}
  .logo{left:68px;top:62px;display:flex;align-items:center;gap:8px}
  .logo .mark{width:37px;height:37px;background:var(--brand)}
  .logo .name{font-family:"Open Sans",sans-serif;font-weight:600;font-size:34px;color:var(--brand);letter-spacing:1px;line-height:1}
  .nav a{position:absolute;top:73px;font-size:13px;color:#1b1b1b;text-decoration:none;font-family:"Arimo",sans-serif}
  .nav .active{left:460px;top:69px;width:56px;height:23px;background:var(--navy);color:#fff;text-align:center;padding-top:4px;border-radius:2px}

  .hero{left:0;top:117px;width:1015px;height:307px;background:radial-gradient(ellipse at 60% 50%,#fff 0%,var(--hero-bg) 75%)}
  .arrow{width:22px;height:22px;border-radius:50%;background:#888;top:259px}
  .arrow svg{position:absolute;left:6px;top:6px}
  .hero-art{left:181px;top:132px;width:274px;height:256px;background:linear-gradient(120deg,#2e2e2e 0%,#5a5a5a 45%,#e6e6e6 55%,#f4f4f4 100%);border-radius:14px}
  .hero-title{left:505px;top:164px;font-family:"Open Sans",sans-serif;font-weight:600;font-size:19.5px;color:#333}
  .hero-copy{left:505px;top:198px;width:356px;font-size:11px;line-height:19.4px;text-align:justify}
  .cta{left:506px;top:286px;width:205px;height:39px;background:linear-gradient(#4a4a4a,#262626);border-radius:3px;color:#fff;font-family:"Open Sans",sans-serif;font-weight:600;font-size:14.5px;letter-spacing:.3px;padding:9px 0 0 15px}
  .cta span{position:absolute;right:11px;top:9px;width:20px;height:20px;border-radius:50%;background:#777}
  .cta svg{position:absolute;left:7px;top:6px}
  .badge{top:347px;width:100px;height:32px;border-radius:3px}
  .badge.one{left:506px;background:#6b6b6b}
  .badge.two{left:612px;background:#222}
  .hero-shadow{left:80px;top:424px;width:855px;height:14px;background:radial-gradient(ellipse at 50% 0,rgba(0,0,0,.12),rgba(0,0,0,0) 70%)}

  .about-title{left:85px;top:464px;font-family:"Open Sans",sans-serif;font-weight:600;font-size:16px;color:var(--title)}
  .about-copy{left:85px;top:492px;width:681px;font-size:11px;line-height:19.4px;text-align:justify}
  .about-art{left:794px;top:455px;width:137px;height:154px;background:linear-gradient(160deg,#e9eef4,#c9d4e2 60%,#2b4b7c);border-radius:6px}
  .rule{left:85px;top:634px;width:846px;height:1px;background:linear-gradient(90deg,rgba(0,0,0,0),#ddd 15%,#ddd 85%,rgba(0,0,0,0))}

  .service .icon{position:absolute;width:57px;height:71px;border-radius:6px}
  .service h3{position:absolute;font-family:"Open Sans",sans-serif;font-weight:600;font-size:16.5px;color:var(--title);white-space:nowrap}
  .service p{position:absolute;width:187px;font-size:11px;line-height:16px;text-align:justify}
  .service .more{position:absolute;width:253px;height:29px;background:linear-gradient(#f2f2f2,#e4e4e4);font-size:10px;color:#555;text-align:center;padding-top:9px}

  .footer{left:0;top:931px;width:1015px;height:209px;background:var(--footer-bg)}
  .footcol{top:950px;width:180px}
  .footcol h4{font-weight:400;font-size:12px;color:var(--footer-head);margin-bottom:9px}
  .footcol li{list-style:none;font-size:11.5px;color:var(--footer-link);height:24.7px;padding-left:13px;position:relative}
  .footcol li::before{content:"";position:absolute;left:1px;top:4px;border-left:4px solid #bbb;border-top:3px solid transparent;border-bottom:3px solid transparent}
  .bottombar{left:0;top:1140px;width:1015px;height:60px;background:var(--footer-bottom)}
  .copyright{left:77px;top:1162px;font-size:12px;color:#cfcfcf;word-spacing:2px}
  .social{top:1158px;width:24px;height:24px;border-radius:2px}
</style>
</head>
<body>

<header>
  <div class="abs topbar"></div>
  <div class="abs account">REGISTER &nbsp;|&nbsp; LOG IN</div>
  <div class="abs search">Search
    <svg width="14" height="14" viewBox="0 0 14 14"><circle cx="5.5" cy="5.5" r="4" fill="none" stroke="#333" stroke-width="2"/><line x1="8.5" y1="8.5" x2="13" y2="13" stroke="#333" stroke-width="2.5"/></svg>
  </div>
  <div class="abs lang"><span class="flag"></span>Eng
    <svg width="8" height="5" viewBox="0 0 8 5"><path d="M0 0H8L4 5Z" fill="#333"/></svg>
  </div>

  <div class="abs masthead"></div>
  <div class="abs logo"><span class="mark"></span><span class="name">VEXLO</span></div>
  <nav class="nav">
    <a class="active">HOME</a>
    <a style="left:542px">ABOUT US</a>
    <a style="left:639px">SERVICES</a>
    <a style="left:736px">APLLICATIONS</a>
    <a style="left:859px">CONTACT US</a>
  </nav>
</header>

<section>
  <div class="abs hero"></div>
  <div class="abs arrow" style="left:77px"><svg width="10" height="10" viewBox="0 0 10 10"><path d="M7 1 3 5 7 9" fill="none" stroke="#fff" stroke-width="2"/></svg></div>
  <div class="abs arrow" style="left:918px"><svg width="10" height="10" viewBox="0 0 10 10"><path d="M3 1 7 5 3 9" fill="none" stroke="#fff" stroke-width="2"/></svg></div>
  <div class="abs hero-art" role="img" aria-label="Two smartphones, one dark and one white, with colourful app icons floating beside them"></div>
  <h1 class="abs hero-title">We make Orbit OS and Robo OS Applications</h1>
  <p class="abs hero-copy">Curabitur luctus, sem a rhoncus laoreet, turpis mauris imperdiet odio, nec pellentesque dolor lorem vitae lorem. Nulla sit amet consequat tellus. Donec pharetra iaculis sapien, et fringilla libero mattis in. Nullam accumsan hendrerit tempus.</p>
  <div class="abs cta">VIEW APPLICATIONS<span><svg width="8" height="8" viewBox="0 0 8 8"><path d="M2 0 6 4 2 8" fill="none" stroke="#fff" stroke-width="2"/></svg></span></div>
  <div class="abs badge one"></div>
  <div class="abs badge two"></div>
  <div class="abs hero-shadow"></div>
</section>

<section>
  <h2 class="abs about-title">ABOUT VEXLO</h2>
  <p class="abs about-copy">Aliquam nec sem non elit rhoncus tincidunt at eget purus. In scelerisque nibh commodo enim volutpat vitae pretium lectus ullamcorper. Vivamus dapibus condimentum nisl, sit amet tempus libero vulputate id. Maecenas eleifend ipsum quis elit mollis nec sodales lectus aliquet. Cras dolor dolor, dignissim eu tincidunt sed, interdum eu neque. Aenean eu massa in nibh fringilla convallis non eget lacus. Duis libero elit, porta at consectetur nec, faucibus vitae dolor. Ut a quam et massa dictum venenatis sit amet in sapien. Vivamus eros turpis, gravida fermentum fermentum at, pharetra vitae est. Mauris venenatis condimentum dapibus. Pellentesque id urna pulvinar nulla bibendum vulputate augue vitae hendrerit volutpat, massa erat sodales ante..</p>
  <div class="abs about-art" role="img" aria-label="Smartphone with app icons spilling out beside the company mark"></div>
  <div class="abs rule"></div>
</section>

<section class="services">
  <div class="service">
    <div class="icon" style="left:84px;top:662px;background:linear-gradient(#555,#1e1e1e)" role="img" aria-label="Black smartphone"></div>
    <h3 style="left:151px;top:656px">Pocketphone Applications</h3>
    <p style="left:151px;top:683px">Pellentesque id urna pulvinar nulla bibendum vulputate augue vitae hendrerit volutpat.</p>
    <div class="more" style="left:84px;top:742px">VIEW MORE &nbsp;»</div>
  </div>
  <div class="service">
    <div class="icon" style="left:380px;top:662px;background:linear-gradient(#a8d14a,#6a9a1e)" role="img" aria-label="Green robot mascot"></div>
    <h3 style="left:448px;top:656px">Robo OS Applications</h3>
    <p style="left:448px;top:683px">Pellentesque id urna pulvinar nulla bibendum vulputate augue vitae hendrerit volutpat.</p>
    <div class="more" style="left:380px;top:742px">VIEW MORE &nbsp;»</div>
  </div>
  <div class="service">
    <div class="icon" style="left:677px;top:662px;background:linear-gradient(#f2f2f2,#c4c4c4)" role="img" aria-label="Silver system lettering"></div>
    <h3 style="left:744px;top:656px">Orbit OS Applications</h3>
    <p style="left:744px;top:683px">Pellentesque id urna pulvinar nulla bibendum vulputate augue vitae hendrerit volutpat.</p>
    <div class="more" style="left:677px;top:742px">VIEW MORE &nbsp;»</div>
  </div>

  <div class="service">
    <div class="icon" style="left:84px;top:799px;background:linear-gradient(#eee,#a9b0b8)" role="img" aria-label="Silver padlock"></div>
    <h3 style="left:151px;top:793px">MobileSecurity Apps</h3>
    <p style="left:151px;top:820px">Pellentesque id urna pulvinar nulla bibendum vulputate augue vitae hendrerit volutpat.</p>
    <div class="more" style="left:84px;top:879px">VIEW MORE &nbsp;»</div>
  </div>
  <div class="service">
    <div class="icon" style="left:380px;top:799px;background:linear-gradient(135deg,#e8502a,#f0b030 45%,#5aa83a 70%,#3a78c8)" role="img" aria-label="Colourful 3D chart"></div>
    <h3 style="left:448px;top:793px">Business Type Apps</h3>
    <p style="left:448px;top:820px">Pellentesque id urna pulvinar nulla bibendum vulputate augue vitae hendrerit volutpat.</p>
    <div class="more" style="left:380px;top:879px">VIEW MORE &nbsp;»</div>
  </div>
  <div class="service">
    <div class="icon" style="left:677px;top:799px;background:linear-gradient(#6bc3ee,#1e4f8c)" role="img" aria-label="Phone with splashing water"></div>
    <h3 style="left:744px;top:793px">Lifestyle Apps</h3>
    <p style="left:744px;top:820px">Pellentesque id urna pulvinar nulla bibendum vulputate augue vitae hendrerit volutpat.</p>
    <div class="more" style="left:677px;top:879px">VIEW MORE &nbsp;»</div>
  </div>
</section>

<footer>
  <div class="abs footer"></div>
  <div class="abs footcol" style="left:77px"><h4>Footer Links Header</h4><ul><li>Aliquam nec</li><li>Duis ultriciessem</li><li>Aliquam vehi</li><li>Etiam euismod</li><li>Nulla lobortis dolo</li><li>Nunc a scelerisque</li></ul></div>
  <div class="abs footcol" style="left:264px"><h4>Footer Links Header</h4><ul><li>Aliquam nec</li><li>Duis ultriciessem</li><li>Aliquam vehi</li><li>Etiam euismod</li><li>Nulla lobortis dolo</li><li>Nunc a scelerisque</li></ul></div>
  <div class="abs footcol" style="left:451px"><h4>Footer Links Header</h4><ul><li>Aliquam nec</li><li>Duis ultriciessem</li><li>Aliquam vehi</li><li>Etiam euismod</li><li>Nulla lobortis dolo</li><li>Nunc a scelerisque</li></ul></div>
  <div class="abs footcol" style="left:637px"><h4>Footer Links Header</h4><ul><li>Aliquam nec</li><li>Duis ultriciessem</li><li>Aliquam vehi</li><li>Etiam euismod</li><li>Nulla lobortis dolo</li><li>Nunc a scelerisque</li></ul></div>
  <div class="abs footcol" style="left:824px"><h4>Footer Links Header</h4><ul><li>Aliquam nec</li><li>Duis ultriciessem</li><li>Aliquam vehi</li><li>Etiam euismod</li><li>Nulla lobortis dolo</li><li>Nunc a scelerisque</li></ul></div>

  <div class="abs bottombar"></div>
  <div class="abs copyright">Copyright &copy; 2013 &nbsp;www.vexlo.com &nbsp;&nbsp;All rights reserved.</div>
  <div class="abs social" style="left:827px;background:#4aa8e0"></div>
  <div class="abs social" style="left:857px;background:#3b5b9a"></div>
  <div class="abs social" style="left:887px;background:#1d78b4"></div>
  <div class="abs social" style="left:916px;background:#444"></div>
</footer>

</body>
</html>
```